Scrap Metal Company Require Brochure for presentation to prospective client

We are a scrap metal company based in Singapore.
We require a brochure of about 4 pages, 1) Cover Page, 2 and 3 is the material we deal in and services we provide and 4) a backpage.
Brochure will be presented to prospective and selected local supplier to present to them the type of products we deal in and the type of services we provide. Purpose is to convince the prospective client to engage our services and also to sell us their scrap metal.
http://www.pelrowanmetals.com/our-services/for-corporate <- This link is for the intended audience of this brochure.
Designer is welcome to take any images from my website or use their own images in the design. Preferably, should the designer choose to use scrap metal images, please try to mainly use pictures of aluminium scrap, copper scrap, stainless steel scrap and ferrous scrap.
Attached is our company logo and some pictures of the scrap. www.pelrowanmetals.com is our website.
The design should give the audience a feeling of confidence, professionalism, honesty and trust in us.
This brochure is intended to be A4 Sizer
Target Market(s)
Local manufacturing company that does metal fabrication with off-cut scrap during the manufacturing process
Industry/Entity Type
Steel
Look and feel

```html
<!DOCTYPE html>
<html lang="en">
<head>
<meta charset="utf-8">
<title>Pelrowan Metals Recycling – Inside Spread</title>
<link href="https://fonts.googleapis.com/css2?family=Arimo:wght@400;700&display=swap" rel="stylesheet">
<style>
:root{
  --stage:#a9a9a9;
  --paper:#ffffff;
  --paper-shade:#ececec;
  --gold:#c8922a;
  --gold-light:#e0ac2c;
  --gold-dark:#b8861c;
  --ink:#2b2b2b;
  --ink-soft:#444;
  --rule:#d2a448;
  --arrow:#f2c400;
}
*{box-sizing:border-box;margin:0;padding:0}
html,body{width:1200px;height:727px;overflow:hidden}
body{background:var(--stage);font-family:"Arimo",Arial,sans-serif;color:var(--ink);position:relative}
.spread{position:absolute;left:123px;top:27px;width:952px;height:673px;display:flex}
.page{position:relative;width:476px;height:673px;background:radial-gradient(ellipse at 70% 20%,#fff 0,#fff 40%,var(--paper-shade) 100%)}
.page--left{background:linear-gradient(90deg,#fafafa 0,#fff 80%,#e3e3e3 100%)}
.page--right{background:linear-gradient(90deg,#dedede 0,#fafafa 12%,#fff 60%,#f0f0f0 100%)}
.abs{position:absolute}
.h1{font-size:15.5px;font-weight:700;color:var(--gold)}
.h2{font-size:13.5px;color:var(--gold);border-bottom:1px solid var(--rule);padding-bottom:1px}
.h3{font-size:9.5px;font-weight:700;color:var(--gold);border-bottom:1px solid var(--rule);text-transform:uppercase;padding-bottom:1px}
.body{font-size:7.4px;line-height:1.25;color:var(--ink-soft)}
.body p{margin-bottom:8px}
.step h4{font-size:9.2px;font-weight:700;color:var(--ink);margin-bottom:2px}
.step p{font-size:7.4px;line-height:1.22;color:var(--ink-soft)}
.grade h4{font-size:9px;font-weight:700;margin-bottom:2px}
.grade p{font-size:5.6px;line-height:1.22;color:var(--ink-soft)}
.swatch{position:absolute;border-radius:50%;border:4px solid var(--gold-light);box-shadow:0 0 0 1px #c59b45}
.tags{position:absolute;display:flex;gap:3px}
.tag{height:18px;padding:0 6px;background:linear-gradient(#e4b33a,var(--gold-dark));font-size:8.2px;font-weight:700;color:#2a1e05;display:flex;align-items:center;justify-content:center}
.flow-box{position:absolute;background:#fff;border:1px solid #b9b9b9;font-size:7.6px;font-weight:700;text-align:center;display:flex;align-items:center;justify-content:center;line-height:1.2;padding:0 6px}
</style>
</head>
<body>
<div class="spread">
  <section class="page page--left">
    <h1 class="abs h1" style="left:34px;top:23px">Our Company</h1>
    <div class="abs body" style="left:34px;top:44px;width:420px">
      <p>Pelrowan Metals Recycling is a privately-held company located in Singapore with a humble beginning. We has grown rapidly through the continuous support of our customer and suppliers and currently have supplier across various industries including, general public, constructions, manufacturers, engineering, demolition, shipyards, other recycling yards and overseas customer.</p>
      <p>Pelrowan Metals Recycling has become a recycling industry leader in the local market, committed to responsibly and efficiently serving all its customer, supplier and community with integrity and professionalism, and in an environmentally safe manner.</p>
      <p>We are committed to our suppliers and consumers by effectively sourcing, processing, and marketing scrap metal for recycling. We actively pursue new and long lasting relationships by partnering with our customers, providing quality service built upon integrity, honesty, and professionalism. We are committed to meeting all our customers needs by exceeding their expectations.</p>
    </div>

    <h2 class="abs h2" style="left:34px;top:135px;width:418px">Process</h2>
    <div class="abs step" style="left:34px;top:155px;width:200px"><h4>PROCUREMENT &amp; COLLECTION</h4><p>Purchase from both our local (companies &amp; individual) and overseas sources for transporting of scrap material to our scrap yard.</p></div>
    <div class="abs step" style="left:249px;top:155px;width:190px"><h4>SORTING &amp; SEGREGATION</h4><p>At our yard, all items will be sorted into different categories and grade.</p></div>
    <div class="abs step" style="left:34px;top:202px;width:200px"><h4>FERROUS SCRAP</h4><p>After sorting and segregation, all ferrous scrap will be shear and cut to improve density and remove of other impurities.</p></div>
    <div class="abs step" style="left:249px;top:202px;width:190px"><h4>NON-FERROUS SCRAP</h4><p>All non-ferrous scrap will be processed to remove any impurities and subsequently, send for baling barquetting or packing into jumbo bags.</p></div>
    <div class="abs step" style="left:34px;top:250px;width:200px"><h4>QUALITY CONTROL</h4><p>Both ferrous and non-ferrous scrap will be inspected closely to ensure the quality of the processed scrap material.</p></div>
    <div class="abs step" style="left:249px;top:250px;width:200px"><h4>STORAGE/SALE</h4><p>Item will be stored within our premises or sent to our</p></div>

    <h2 class="abs h2" style="left:34px;top:297px;width:418px">Copper / Brass</h2>
    <div class="swatch" role="img" aria-label="Photo of bare copper wire scrap" style="left:33px;top:322px;width:62px;height:62px;background:radial-gradient(#c27b3e,#7a3f16)"></div>
    <div class="abs grade" style="left:96px;top:326px;width:64px"><h4>BARLEY</h4><p>Shall consist of No. 1 bare, uncoated, unalloyed copper wire, not smaller than No. 16 B &amp; S Wire gauge.</p></div>
    <div class="swatch" role="img" aria-label="Photo of copper clippings scrap" style="left:154px;top:322px;width:62px;height:62px;background:radial-gradient(#d08a5a,#8b3f22)"></div>
    <div class="abs grade" style="left:217px;top:326px;width:75px"><h4>BERRY CANDY</h4><p>Shall Consist of clean, untinned, uncoated, unalloyed copper wire, clippings, punchings, bus bars, commutator segment not less than 1/6 of an inch thick, free of burnt wire which is brittle.</p></div>
    <div class="swatch" role="img" aria-label="Photo of mixed yellow brass scrap" style="left:289px;top:322px;width:62px;height:62px;background:radial-gradient(#b9a98a,#5b4d35)"></div>
    <div class="abs grade" style="left:352px;top:326px;width:100px"><h4>BRASS (HONEY)</h4><p>Shall consist of Mixed yellow brass solids, including brass castings, rolled brass, rod brass, tubing and misc yellow brasses, including plated brass. Free of manganese-bronze, aluminum-bronze, unsweated radiators or radiator parts, iron, and excessively dirty and corroded materials. Free from any type of munitions.</p></div>
    <div class="swatch" role="img" aria-label="Photo of unalloyed copper wire scrap" style="left:33px;top:400px;width:62px;height:62px;background:radial-gradient(#a86a3e,#5a3218)"></div>
    <div class="abs grade" style="left:96px;top:404px;width:165px"><h4>BIRCH/CLIFF</h4><p>Shall consist of Misc, unalloyed copper scrap having a nominal 96% copper content (min 94%) as determined by electrolytic assay. Should be free of the following: Excessively leaded, tinned, soldered copper wire; brass and bronze wire; excessive oil content, iron, and non-metallics; copper wire from burning, containing insulation; hair wire, burnt wire which is brittle and reasonably free of ash.</p></div>
    <div class="swatch" role="img" aria-label="Photo of yellow brass clippings" style="left:260px;top:400px;width:62px;height:62px;background:radial-gradient(#d8c07a,#7d6a35)"></div>
    <div class="abs grade" style="left:323px;top:404px;width:125px"><h4>BRASS NEW CLIPPINGS</h4><p>Shall consist of cuttings of new unleaded yellow brass sheet or plate, to be clean and free from foreign substances. To be free of Muntz metal and naval brass</p></div>

    <h2 class="abs h2" style="left:34px;top:467px;width:215px">Aluminium / Stainless / Alloy</h2>
    <div class="tags" style="left:33px;top:487px"><span class="tag">Extrusion 6063</span><span class="tag">Tough Taboo</span><span class="tag">Taint Tabor</span><span class="tag">Tense</span><span class="tag">Telic</span><span class="tag">Stainless Steel 304/316</span><span class="tag">Molybdenum</span></div>
    <h2 class="abs h2" style="left:34px;top:511px;width:215px">Ferrous</h2>
    <div class="tags" style="left:33px;top:531px"><span class="tag" style="width:66px">I / H Beam</span><span class="tag">No. 1 Heavy Melting Steel (HMS 1)</span></div>
    <h2 class="abs h2" style="left:34px;top:555px;width:215px">Machinery</h2>
    <div class="tags" style="left:33px;top:575px;gap:6px"><span class="tag" style="width:67px">Machinery</span><span class="tag" style="width:114px">Drilling, Tools and ETC</span><span class="tag" style="width:132px">Welding Machine, Torch Etc</span><span class="tag" style="width:92px">Distribution Box</span></div>
    <h2 class="abs h2" style="left:34px;top:598px;width:215px">Electronics</h2>
    <div class="tags" style="left:33px;top:619px;gap:6px"><span class="tag" style="width:95px">Motherboard Scrap</span><span class="tag" style="width:98px">Mixed Board Scrap</span><span class="tag" style="width:86px">Hard Disk Scrap</span><span class="tag" style="width:114px">Electronic Device Scrap</span></div>
    <h2 class="abs h1" style="left:34px;top:640px;font-weight:400;font-size:13.5px">Industrial Surplus / Reject / Others</h2>
  </section>

  <section class="page page--right">
    <h1 class="abs h1" style="left:26px;top:23px">Our Services</h1>
    <h3 class="abs h3" style="left:26px;top:42px;width:420px">For Individual</h3>
    <div class="abs body" style="left:26px;top:58px;width:424px">
      <p>We serve the general public mainly by the walk in channel. To serve you better, we have extended our collection hours!</p>
      <p>Monday to Friday: 0830Hrs to 1800Hrs<br>Saturday: 0830Hrs to 1800Hrs</p>
      <p>Can’t make it within the operating hour? Give us a call and we will make the necessary arrangement for you!</p>
      <p>At our yard, our friendly staff will assist you in the sorting and separating of your scrap material into different grade so you can be sure you get the most value out of your scrap.</p>
    </div>
    <h3 class="abs h3" style="left:26px;top:150px;width:420px">For Corporate</h3>
    <div class="abs body" style="left:26px;top:167px;width:428px">
      <p>Pelrowan Metals Recycling provides excellent service and very competitive pricing for your scrap materials.<br>Some of the services we provide are as follows:</p>
      <p>Roll-off Open Top Container (OTC), small container, customized container for the disposal of your scrap material at your premises. Arrangement can also be made should you require container to be place at other permanent or temporary work site.</p>
      <p>Fast and convenient service for collection. We provide regular schedule pick-up or just call us when the bin is full!</p>
      <p>Our company provide weighing upon collection with our accurately calibrated crane scale so you always know the weight of your material before leaving the premises.</p>
      <p>Should your company scrap contain confidential information, or rejected material that requires to be destroy, you are welcome to visit our scrap yard to witness the destruction process, alternatively, we can send you a photographic image as proof.</p>
      <p>&nbsp; &nbsp; &nbsp; &nbsp; &nbsp; We provide prompt payment and very competitive price. Even if you need payment upon collection, just let us know.</p>
      <p>&nbsp; Should you have other requirement on top of your scrap collection, e.g. waste collection, we will be more than please to offer any solutions or to accommodate to your request.</p>
      <p>&nbsp; &nbsp; &nbsp; Companies are also welcome to unload their scrap material at our scrap yard.</p>
      <p>Write us an email here or fill up the form below today to understand how we can be at your service or for a non-obliging quotation for your scrap material. We will contact you promptly!</p>
    </div>
    <h3 class="abs h3" style="left:26px;top:408px;width:420px">For International</h3>
    <div class="abs body" style="left:26px;top:426px;width:428px">
      <p>Pelrowan Metals Recycling have strong relationship with all our international customer, allowing both parties to established long term mutually beneficial relationship.</p>
      <p>We believe in providing top quality material to our buyer and in turn, our buyer will provide us with the most competitive price to allow staying competitive in our various markets, procuring larger quantity of material which will in turn, be sold to our buyer.</p>
    </div>

    <svg class="abs" style="left:0;top:0" width="476" height="673" aria-hidden="true">
      <g fill="none" stroke="var(--arrow)" stroke-width="7">
        <path d="M62 552 V528 H98"/>
        <path d="M361 524 H378 V548"/>
        <path d="M378 600 V628 H338"/>
        <path d="M100 628 H64 V608"/>
      </g>
      <g fill="var(--arrow)">
        <path d="M98 521 L108 528 L98 535Z"/>
        <path d="M371 548 L378 558 L385 548Z"/>
        <path d="M338 621 L328 628 L338 635Z"/>
        <path d="M57 608 L64 598 L71 608Z"/>
      </g>
    </svg>
    <div class="flow-box" style="left:138px;top:515px;width:198px;height:25px">Our Company Supply Top Quality Material</div>
    <div class="flow-box" style="left:3px;top:566px;width:175px;height:28px">Pelrowan Metals Process and Sort Material to Match Customer Requirement</div>
    <div class="flow-box" style="left:249px;top:566px;width:176px;height:28px">Buyer Provide Competitive Price to Our Company</div>
    <div class="flow-box" style="left:119px;top:614px;width:190px;height:38px">Pelrowan Metals Recycling Provide Competitive Price to all Existing and New Customer to Procure More Material</div>
  </section>
</div>
</body>
</html>
```